Bref créative
Brookmere
Brookmere Vale Baptist Church
Simple
Dolores Lomax
Communications
4163 Ambervale Road
Regina SK S7N 3K8
dolores@brookmerechapel.ca
brookmerechapel.ca
We will need business cards, letterhead and envelopes.
Our Logo
ai file

```html
<!DOCTYPE html>
<html lang="en">
<head>
<meta charset="utf-8">
<title>Brookmere Vale Baptist Church — Stationery</title>
<link rel="stylesheet" href="https://fonts.googleapis.com/css2?family=Cinzel:wght@500&family=Lato:wght@400;700&display=swap">
<style>
  :root {
    --backdrop: #2b2b2b;
    --paper: #ffffff;
    --blue-deep: #1f5f8a;
    --blue-mid: #3a86b4;
    --blue-light: #6fb0d6;
    --ink: #5d6770;
    --tagline: #7f8a93;
  }
  * { margin: 0; padding: 0; box-sizing: border-box; }
  html, body { width: 1200px; height: 667px; overflow: hidden; }
  body { background: var(--backdrop); position: relative; font-family: "Lato", sans-serif; }

  .piece { position: absolute; background: var(--paper); box-shadow: 0 4px 14px rgba(0,0,0,.55); overflow: hidden; }

  .wordmark { font-family: "Cinzel", serif; font-weight: 500; color: var(--blue-deep); letter-spacing: 1px; line-height: 1; text-align: center; }
  .tagline { font-family: "Lato", sans-serif; color: var(--tagline); text-align: center; letter-spacing: .5px; }

  .band { background: linear-gradient(90deg, var(--blue-deep), var(--blue-mid) 50%, var(--blue-deep)); }
  .contact-line { font-size: 6px; color: var(--ink); text-align: center; letter-spacing: .3px; }

  /* Business card front */
  .card-front { left: 34px; top: 216px; width: 199px; height: 163px; }
  .card-front .band-top { height: 16px; display: flex; align-items: center; justify-content: center; color: #e6f2fa; font-size: 7px; letter-spacing: .4px; }
  .card-front .wordmark { font-size: 26px; margin-top: 14px; }
  .card-front .tagline { font-size: 6px; margin-top: 5px; }
  .card-front .card-contact { position: absolute; left: 0; right: 0; bottom: 20px; }
  .card-front .contact-line { font-size: 5.5px; line-height: 9px; }
  .card-front .band-bottom { position: absolute; left: 0; right: 0; bottom: 0; height: 10px; }

  /* Business card back */
  .card-back { left: 34px; top: 384px; width: 199px; height: 163px;
    background: radial-gradient(ellipse at 50% 45%, var(--blue-light), var(--blue-mid) 45%, var(--blue-deep)); }
  .card-back .wordmark { color: rgba(255,255,255,.35); font-size: 30px; margin-top: 40px; }
  .card-back .strip { position: absolute; left: 0; right: 0; top: 0; height: 12px; background: rgba(10,40,70,.35); }

  /* Letterhead */
  .letterhead { left: 254px; top: 19px; width: 370px; height: 629px; }
  .letterhead .band-top { height: 12px; }
  .letterhead .wordmark { font-size: 30px; margin-top: 18px; }
  .letterhead .tagline { font-size: 7px; margin-top: 6px; }
  .letterhead .contact-line { position: absolute; left: 0; right: 0; bottom: 22px; }
  .letterhead .band-bottom { position: absolute; left: 0; right: 0; bottom: 0; height: 14px;
    display: flex; align-items: center; justify-content: center; color: #e6f2fa; font-size: 6px; }

  /* Envelope back */
  .envelope-back { left: 643px; top: 110px; width: 540px; height: 238px; }
  .envelope-back svg { position: absolute; inset: 0; }
  .envelope-back .flap-mark { position: absolute; left: 0; right: 0; top: 56px; font-size: 13px; color: #c9b98e; }

  /* Envelope front */
  .envelope-front { left: 643px; top: 413px; width: 540px; height: 235px; }
  .envelope-front .band-top { height: 14px; }
  .envelope-front .wordmark { font-size: 30px; margin-top: 24px; }
  .envelope-front .tagline { font-size: 7px; margin-top: 6px; }
  .envelope-front .contact-line { position: absolute; left: 0; right: 0; bottom: 22px; }
  .envelope-front .band-bottom { position: absolute; left: 0; right: 0; bottom: 0; height: 13px;
    display: flex; align-items: center; justify-content: center; color: #e6f2fa; font-size: 6px; }
</style>
</head>
<body>

  <section class="piece card-front" aria-label="Business card front">
    <div class="band band-top">Dolores Lomax · Communications</div>
    <div class="wordmark">Brookmere</div>
    <div class="tagline">Brookmere Vale Baptist Church</div>
    <div class="card-contact">
      <p class="contact-line">4163 Ambervale Road, Regina SK S7N 3K8</p>
      <p class="contact-line">dolores@brookmerechapel.ca · T 306 555 0148</p>
    </div>
    <div class="band band-bottom"></div>
  </section>

  <section class="piece card-back" aria-label="Business card back">
    <div class="strip"></div>
    <div class="wordmark">Brookmere</div>
  </section>

  <section class="piece letterhead" aria-label="Letterhead">
    <div class="band band-top"></div>
    <div class="wordmark">Brookmere</div>
    <div class="tagline">Brookmere Vale Baptist Church</div>
    <p class="contact-line">4163 Ambervale Road, Regina SK S7N 3K8 · dolores@brookmerechapel.ca · T 306 555 0148 · F 306 555 0149</p>
    <div class="band band-bottom">brookmerechapel.ca</div>
  </section>

  <section class="piece envelope-back" aria-label="Envelope back">
    <svg width="540" height="238" viewBox="0 0 540 238">
      <path d="M0 0 L230 118 Q270 136 310 118 L540 0" fill="none" stroke="#d6d9dc" stroke-width="1.5"/>
      <path d="M0 238 L200 120 M540 238 L340 120" fill="none" stroke="#e4e6e8" stroke-width="1"/>
    </svg>
    <div class="wordmark flap-mark">Brookmere</div>
  </section>

  <section class="piece envelope-front" aria-label="Envelope front">
    <div class="band band-top"></div>
    <div class="wordmark">Brookmere</div>
    <div class="tagline">Brookmere Vale Baptist Church</div>
    <p class="contact-line">4163 Ambervale Road, Regina SK S7N 3K8 · dolores@brookmerechapel.ca · T 306 555 0148 · F 306 555 0149</p>
    <div class="band band-bottom">brookmerechapel.ca</div>
  </section>

</body>
</html>
```